Price sign

Looking for a fresh new pricing sign.. with new prices size 2ft tall x 4ft wide , express lube $40.95, automatic transmission $129.95, radiator $109.95, Torvex plus express lube $79.95, std trans/ diff $79.95, tuneup 4cyl $149.95, 6cyl $175.95 ,

```html
<!DOCTYPE html>
<html lang="en">
<head>
<meta charset="utf-8">
<title>Service Price Sign</title>
<link href="https://fonts.googleapis.com/css2?family=Roboto+Slab:wght@800;900&family=Poppins:ital,wght@0,700;1,500&family=Caveat+Brush&display=swap" rel="stylesheet">
<style>
  :root {
    --gold-deep: #f4c443;
    --gold-light: #efd97f;
    --blue-bright: #1a80c9;
    --blue-mid: #283f92;
    --blue-deep: #2c2f6c;
    --red: #f6474a;
    --yellow-text: #fde20a;
    --ink: #0b0b0b;
    --white: #ffffff;
    --page: #ffffff;
  }
  * { margin: 0; padding: 0; box-sizing: border-box; }
  html, body { width: 1200px; height: 1200px; overflow: hidden; background: var(--page); }
  .sign { position: absolute; left: 0; top: 300px; width: 1200px; height: 600px; }
  .panel { position: absolute; width: 400px; height: 300px; overflow: hidden; }
  .panel--gold .backdrop { background: radial-gradient(circle at 30% 70%, var(--gold-deep), var(--gold-light) 75%); }
  .panel--blue .backdrop { background: linear-gradient(120deg, var(--blue-bright) 0%, var(--blue-mid) 45%, var(--blue-deep) 80%); }
  .backdrop { position: absolute; inset: 0; }

  .title {
    position: absolute; left: 0; right: 0; text-align: center; white-space: nowrap;
    font-family: "Roboto Slab", Georgia, serif; font-weight: 900;
    font-size: 42px; line-height: 50px; letter-spacing: 1px;
  }
  .panel--gold .title { color: var(--ink); }
  .panel--blue .title { color: var(--yellow-text); }
  .title .small { display: block; font-size: 20px; line-height: 18px; }
  .title .mid { display: block; font-size: 34px; line-height: 32px; letter-spacing: 0.5px; }

  .band { position: absolute; left: 6px; width: 378px; height: 56px; }
  .band svg { position: absolute; inset: 0; width: 100%; height: 100%; }
  .band-text { position: absolute; inset: 0; display: flex; flex-direction: column; align-items: center; justify-content: center; color: var(--white); }
  .band-lead { font-family: "Poppins", Arial, sans-serif; font-weight: 700; font-size: 16px; line-height: 20px; }
  .band-interval { font-family: "Caveat Brush", cursive; font-size: 21px; line-height: 22px; font-style: italic; letter-spacing: 0.8px; }

  .price { position: absolute; display: flex; align-items: flex-start; }
  .price .from { font-family: "Poppins", Arial, sans-serif; font-style: italic; font-weight: 500; font-size: 10px; margin-top: 4px; margin-right: 2px; }
  .price .amount { font-family: "Caveat Brush", cursive; font-size: 76px; line-height: 62px; }
  .price .tail { display: flex; flex-direction: column; margin-left: 2px; }
  .price .cents { font-family: "Caveat Brush", cursive; font-size: 36px; line-height: 34px; }
  .price .tax { font-family: "Poppins", Arial, sans-serif; font-style: italic; font-weight: 500; font-size: 9px; margin-top: 2px; }
  .price--red { color: var(--red); }
  .price--white { color: var(--white); }
  .price--compact .amount { font-size: 64px; line-height: 54px; }
  .price--compact .cents { font-size: 30px; line-height: 30px; }

  .cyl-label { position: absolute; font-family: "Roboto Slab", Georgia, serif; font-weight: 900; font-size: 26px; line-height: 30px; color: var(--yellow-text); transform: translateX(-50%); }
  .divider { position: absolute; left: 200px; top: 205px; width: 2px; height: 80px; background: var(--white); }
</style>
</head>
<body>
<svg width="0" height="0" style="position:absolute">
  <defs>
    <path id="brush" d="M14 8 L370 4 L378 12 L366 18 L376 24 L364 32 L372 40 L362 47 L368 54 L20 52 L26 46 L2 44 L14 38 L6 30 L16 24 L0 18 L18 14 Z"/>
  </defs>
</svg>

<main class="sign">
  <section class="panel panel--gold" style="left:0;top:0">
    <div class="backdrop" role="img" aria-label="Faded engine parts background in warm gold tones"></div>
    <h2 class="title" style="top:20px">EXPRESS<br>LUBE</h2>
    <div class="band" style="top:143px"><svg viewBox="0 0 378 56" preserveAspectRatio="none"><use href="#brush" fill="var(--red)"/></svg>
      <div class="band-text"><span class="band-lead">14 POINT SERVICE</span><span class="band-interval">SERVICE EVERY 3000 MILES</span></div></div>
    <div class="price price--red" style="left:102px;top:228px"><span class="from">FROM</span><span class="amount">$40.</span><span class="tail"><span class="cents">95</span><span class="tax">PLUS TAX</span></span></div>
  </section>

  <section class="panel panel--blue" style="left:400px;top:0">
    <div class="backdrop" role="img" aria-label="Faded transmission parts background in blue tones"></div>
    <h2 class="title" style="top:20px">AUTOMATIC<br>TRANSMISSION</h2>
    <div class="band" style="top:142px"><svg viewBox="0 0 378 56" preserveAspectRatio="none"><use href="#brush" fill="var(--red)"/></svg>
      <div class="band-text"><span class="band-lead">30 MINUTE SERVICE</span><span class="band-interval">SERVICE EVERY 25,000 MILES</span></div></div>
    <div class="price price--white" style="left:99px;top:218px"><span class="from">FROM</span><span class="amount">$129.</span><span class="tail"><span class="cents">95</span><span class="tax">PLUS TAX</span></span></div>
  </section>

  <section class="panel panel--gold" style="left:800px;top:0">
    <div class="backdrop" role="img" aria-label="Faded radiator parts background in warm gold tones"></div>
    <h2 class="title" style="top:35px">RADIATOR</h2>
    <div class="band" style="top:142px"><svg viewBox="0 0 378 56" preserveAspectRatio="none"><use href="#brush" fill="var(--red)"/></svg>
      <div class="band-text"><span class="band-lead">30 MINUTE SERVICE</span><span class="band-interval">SERVICE EVERY 25,000 MILES</span></div></div>
    <div class="price price--white" style="left:102px;top:218px"><span class="from">FROM</span><span class="amount">$109.</span><span class="tail"><span class="cents">95</span><span class="tax">PLUS TAX</span></span></div>
  </section>

  <section class="panel panel--blue" style="left:0;top:300px">
    <div class="backdrop" role="img" aria-label="Faded engine parts background in blue tones"></div>
    <h2 class="title" style="top:20px;font-size:40px">TORVEX PLUS<br>EXPRESS</h2>
    <div class="band" style="top:141px"><svg viewBox="0 0 378 56" preserveAspectRatio="none"><use href="#brush" fill="var(--red)"/></svg>
      <div class="band-text"><span class="band-lead">14 POINT SERVICE</span><span class="band-interval">SERVICE EVERY 3000 MILES</span></div></div>
    <div class="price price--white" style="left:95px;top:226px"><span class="from">FROM</span><span class="amount">$79.</span><span class="tail"><span class="cents">95</span><span class="tax">PLUS TAX</span></span></div>
  </section>

  <section class="panel panel--gold" style="left:400px;top:300px">
    <div class="backdrop" role="img" aria-label="Faded drivetrain parts background in warm gold tones"></div>
    <h2 class="title" style="top:40px"><span class="mid">STD TRANSMISION</span><span class="small">OR</span><span class="mid">DIFF SERVICE</span></h2>
    <div class="band" style="top:150px"><svg viewBox="0 0 378 56" preserveAspectRatio="none"><use href="#brush" fill="var(--red)"/></svg>
      <div class="band-text"><span class="band-lead">60 MINUTE SERVICE</span><span class="band-interval">SERVICE EVERY 25000 MILES</span></div></div>
    <div class="price price--red" style="left:115px;top:226px"><span class="from">FROM</span><span class="amount">$79.</span><span class="tail"><span class="cents">95</span><span class="tax">PLUS TAX</span></span></div>
  </section>

  <section class="panel panel--blue" style="left:800px;top:300px">
    <div class="backdrop" role="img" aria-label="Faded engine parts background in blue tones"></div>
    <h2 class="title" style="top:20px">TUNEUP</h2>
    <div class="band" style="top:102px"><svg viewBox="0 0 378 56" preserveAspectRatio="none"><use href="#brush" fill="var(--red)"/></svg>
      <div class="band-text"><span class="band-lead">15 MINUTE SERVICE</span><span class="band-interval">SERVICE EVERY 25,000 MILES</span></div></div>
    <span class="cyl-label" style="left:82px;top:190px">4CYL</span>
    <span class="cyl-label" style="left:304px;top:190px">6CYL</span>
    <div class="divider"></div>
    <div class="price price--white price--compact" style="left:6px;top:222px"><span class="from">FROM</span><span class="amount">$149.</span><span class="tail"><span class="cents">95</span><span class="tax">PLUS TAX</span></span></div>
    <div class="price price--white price--compact" style="left:210px;top:222px"><span class="from">FROM</span><span class="amount">$175.</span><span class="tail"><span class="cents">95</span><span class="tax">PLUS TAX</span></span></div>
  </section>
</main>
</body>
</html>
```